Stainless Steel Business Card

I have a fiber laser and want to highlight its capabilities in a business card. On the card I want

Brevik Industries
Martin Brevik
martin@mbrevik-mail.net
417-555-0163

This will be cut / engraved on stainless steel. I want the Brevik Industries to be prominent with laser cut font so that there are no dropouts on the O and A's. My name email and phone number should be engraved black. I would like some cool geometric patterns to cutout on the card to highlight the capabilities of my machine. I will need to files in the end either SVG or dxf of the engrave portion and the cut portion.

```html
<!DOCTYPE html>
<html lang="en">
<head>
<meta charset="utf-8">
<title>Brevik Industries – Business Card</title>
<link href="https://fonts.googleapis.com/css2?family=Montserrat:wght@400;700;800&display=swap" rel="stylesheet">
<style>
  :root {
    --bg: #2b2b2b;
    --card: #0c0c0c;
    --card-edge: #1c1c1c;
    --silver: #d9d9d9;
    --white: #f4f4f4;
    --pattern-a: #1a1a1a;
    --pattern-b: #2a2a2a;
  }
  * { margin: 0; padding: 0; box-sizing: border-box; }
  html, body {
    width: 1200px;
    height: 1042px;
    overflow: hidden;
    background: var(--bg);
    font-family: "Montserrat", sans-serif;
  }
  .canvas {
    position: relative;
    width: 1200px;
    height: 1042px;
  }
  .card {
    position: absolute;
    left: 320px;
    width: 560px;
    height: 320px;
    background: var(--card);
    border: 1px solid var(--card-edge);
    border-radius: 18px;
    overflow: hidden;
    box-shadow: 0 18px 40px rgba(0,0,0,0.45);
  }
  .card--front { top: 150px; }
  .card--back  { top: 572px; }

  .brand {
    color: var(--silver);
    font-weight: 800;
    text-transform: uppercase;
    line-height: 1;
  }
  .card--front .brand {
    position: absolute;
    inset: 0;
    display: flex;
    flex-direction: column;
    align-items: center;
    justify-content: center;
  }
  .card--front .brand__primary { font-size: 74px; letter-spacing: 4px; }
  .card--front .brand__secondary { font-size: 30px; letter-spacing: 3px; margin-top: 12px; }

  .card--back .brand {
    position: absolute;
    top: 38px;
    right: 40px;
    text-align: right;
  }
  .card--back .brand__primary { font-size: 46px; letter-spacing: 3px; }
  .card--back .brand__secondary { font-size: 19px; letter-spacing: 2px; margin-top: 6px; }

  .pattern-area {
    position: absolute;
    right: 0;
    top: 130px;
    width: 260px;
    height: 190px;
    background: linear-gradient(135deg, var(--pattern-a), var(--pattern-b));
    border-top-left-radius: 40px;
  }

  .contact {
    position: absolute;
    left: 40px;
    bottom: 34px;
    color: var(--white);
  }
  .contact__name {
    font-size: 22px;
    letter-spacing: 1px;
    text-transform: uppercase;
    font-weight: 400;
    margin-bottom: 14px;
  }
  .contact__name strong { font-weight: 700; }
  .contact__list { list-style: none; }
  .contact__item {
    display: flex;
    align-items: center;
    gap: 9px;
    font-size: 15px;
    line-height: 22px;
  }
  .contact__icon { width: 13px; height: 13px; flex: none; }
</style>
</head>
<body>
<main class="canvas">
  <section class="card card--front" aria-label="Card front">
    <div class="brand">
      <span class="brand__primary">Brevik</span>
      <span class="brand__secondary">Industries</span>
    </div>
  </section>

  <section class="card card--back" aria-label="Card back">
    <div class="brand">
      <div class="brand__primary">Brevik</div>
      <div class="brand__secondary">Industries</div>
    </div>

    <div class="pattern-area" role="img" aria-label="Cut-out geometric hexagon outline pattern"></div>

    <div class="contact">
      <p class="contact__name"><strong>Martin</strong> Brevik</p>
      <ul class="contact__list">
        <li class="contact__item">
          <svg class="contact__icon" viewBox="0 0 16 16" fill="var(--white)"><path d="M3 1h3l1.5 4-2 1.2a9 9 0 0 0 4.3 4.3L11 8.5l4 1.5v3a2 2 0 0 1-2 2A12 12 0 0 1 1 3a2 2 0 0 1 2-2z"/></svg>
          417-555-0163
        </li>
        <li class="contact__item">
          <svg class="contact__icon" viewBox="0 0 16 16" fill="none" stroke="var(--white)" stroke-width="1.6"><rect x="1" y="3" width="14" height="10" rx="1.5"/><path d="M1.5 3.8 8 9l6.5-5.2"/></svg>
          martin@mbrevik-mail.net
        </li>
        <li class="contact__item">
          <svg class="contact__icon" viewBox="0 0 16 16" fill="none" stroke="var(--white)" stroke-width="1.4"><circle cx="8" cy="8" r="6.5"/><path d="M1.5 8h13M8 1.5c-2.5 3-2.5 10 0 13M8 1.5c2.5 3 2.5 10 0 13"/></svg>
          www.mbrevik-mail.net
        </li>
      </ul>
    </div>
  </section>
</main>
</body>
</html>
```